Website Header Design

Hi,

We're an electrical company that is looking for a new website header.
Our website is www.brantwoodvoltage.com
We are located in Toronto, Ontario, Canada.
We perform a lot of high rise electrical service work, snow melting system installation in garage ramps, and other general electrical work.
We're willing to change the size of the header and location/look of menus if needed but it is not required. We are hoping to keep our slogan if possible but having it in the header is not a make or break item. Whatever looks better.

Maybe the Toronto skyline could be incorporated somehow but the header also has to have some relevance to an electrical company.
I uploaded png files of the logo but I also have vector files available if needed

Target Market(s)

Property Managers, Contractors, Consulting Engineers

Industry/Entity Type

Electrical

Requirements
Must have
• Our Logo.
Nice to have
• Slogan
Should not have
• Flash

```html
<!DOCTYPE html>
<html lang="en">
<head>
<meta charset="utf-8">
<title>Brantwood Voltage – Website Header</title>
<link rel="stylesheet" href="https://fonts.googleapis.com/css2?family=Roboto+Condensed:wght@700&family=Roboto:wght@500;700&display=swap">
<style>
  :root {
    --panel-dark: #1c1c1c;
    --nav-bg: #3a3a3a;
    --nav-active: #474747;
    --nav-divider: #202020;
    --accent: #f2a51f;
    --text-light: #ffffff;
    --sky-top: #f6c24a;
    --sky-mid: #f4b23a;
    --water: #e89a12;
  }
  * { box-sizing: border-box; margin: 0; padding: 0; }
  html, body { width: 1200px; height: 282px; overflow: hidden; background: var(--panel-dark); }
  .site-header { position: relative; width: 1200px; height: 282px; }
  .brand-panel {
    position: absolute; left: 0; top: 0; width: 224px; height: 282px;
    background: var(--panel-dark);
    display: flex; flex-direction: column; align-items: center; justify-content: flex-end;
    padding-bottom: 30px;
  }
  .brand-mark { width: 70px; height: 70px; background: var(--accent); margin-bottom: 26px; }
  .brand-name {
    font-family: "Roboto", Arial, sans-serif; font-weight: 500; color: var(--text-light);
    font-size: 36px; line-height: 1.08; text-align: center;
  }
  .hero-skyline {
    position: absolute; left: 224px; top: 0; width: 976px; height: 202px;
    background: linear-gradient(180deg, var(--sky-top) 0%, var(--sky-mid) 62%, var(--water) 78%, var(--accent) 100%);
  }
  .slogan {
    position: absolute; right: 32px; top: 34px; text-align: right;
    font-family: "Roboto", Arial, sans-serif; font-weight: 700; color: var(--text-light);
    font-size: 29px; line-height: 1.12;
  }
  .main-nav {
    position: absolute; left: 224px; top: 202px; width: 976px; height: 80px;
    display: flex; background: var(--nav-divider); gap: 3px; padding-top: 3px;
  }
  .nav-item {
    flex: 1; display: flex; align-items: center; justify-content: center;
    background: var(--nav-bg); color: var(--text-light); text-decoration: none;
    font-family: "Roboto Condensed", "Arial Narrow", sans-serif; font-weight: 700; font-size: 24px;
    letter-spacing: -0.3px;
  }
  .nav-item.is-active { background: var(--nav-active); box-shadow: inset 0 -5px 0 var(--accent); }
</style>
</head>
<body>
<header class="site-header">
  <div class="brand-panel">
    <div class="brand-mark"></div>
    <div class="brand-name">Brantwood<br>Voltage</div>
  </div>
  <div class="hero-skyline" role="img" aria-label="Toronto skyline across the lake, tinted in warm orange"></div>
  <p class="slogan">Powerful Solutions.<br>Professional Service.</p>
  <nav class="main-nav">
    <a class="nav-item is-active" href="#">Home</a>
    <a class="nav-item" href="#">About Us</a>
    <a class="nav-item" href="#">Services</a>
    <a class="nav-item" href="#">Projects</a>
    <a class="nav-item" href="#">Clients</a>
    <a class="nav-item" href="#">Contact Us</a>
  </nav>
</header>
</body>
</html>
```